Brandell Law PLLC updated letterhead for solo law practice - legal/professional services

I need a new letterhead design on a word document for my solo law practice. I have attached my current letterhead. Here is my company info:

Douglas Brandell
Brandell Law PLLC
2750 Whitcombe, Suite 410
Dallas, Texas 75219
Phone: 214 555 0186
Email: douglas@brandell-legal.example
Website: www.brandell-legal.example

Preferably I'd like the logo on top followed by my name and email (in the header)

At the bottom (footer) i'd like the rest of the information.

I am fine using a color for the line in between "Brandell" and "Law" in the "Brandell Law" logo. Or a different font.

Industry/Entity Type

Legal

Font styles to use
Serif

Colors

Designer to choose only greyscale colors for use in the design.

Requirements
Must have
• The "Brandell Law" logo with the line in between "Brandell" and "Law" but I am open to ideas on structure and color schemes.
Nice to have
• Logo on top with new color scheme, along with my name and email.
• Address, phone number, web address on bottom.

```html
<!DOCTYPE html>
<html lang="en">
<head>
<meta charset="utf-8">
<title>Brandell Law PLLC — Stationery</title>
<link href="https://fonts.googleapis.com/css2?family=Lora:wght@400&family=Open+Sans:wght@400&family=Roboto:wght@400&family=Roboto+Condensed:wght@400&display=swap" rel="stylesheet">
<style>
  :root {
    --charcoal: #2f2f2f;
    --paper: #fbfbfa;
    --envelope: #ebebea;
    --envelope-shade: #dcdcdb;
    --ink: #4a4a4a;
    --ink-dark: #333333;
    --backdrop: #d9d9d8;
    --white: #ffffff;
  }
  * { box-sizing: border-box; margin: 0; padding: 0; }
  html, body { width: 1200px; height: 801px; overflow: hidden; }
  body { background: var(--backdrop); position: relative; font-family: "Open Sans", sans-serif; }

  .brand-name {
    font-family: "Lora", serif;
    font-weight: 400;
    color: var(--charcoal);
    white-space: nowrap;
    letter-spacing: 0.2px;
  }

  /* Envelope, back with flap */
  .envelope-back {
    position: absolute; left: 95px; top: 335px; width: 451px; height: 229px;
    background: var(--envelope);
  }
  .envelope-back svg { position: absolute; left: 0; top: 0; }
  .envelope-back .brand-name {
    position: absolute; left: 0; right: 0; top: 30px; text-align: center;
    font-size: 23px; color: var(--white);
  }

  /* Envelope, front */
  .envelope-front {
    position: absolute; left: 138px; top: 478px; width: 449px; height: 228px;
    background: var(--envelope);
    box-shadow: -2px 0 3px rgba(0,0,0,0.12);
  }
  .envelope-front .brand-name { position: absolute; left: 31px; top: 24px; font-size: 21px; }
  .envelope-front .return-address {
    position: absolute; left: 31px; top: 52px; width: 150px;
    font-family: "Roboto Condensed", sans-serif; font-size: 8.6px; line-height: 11px; color: var(--ink-dark);
  }
  .envelope-front .edge-band { position: absolute; left: 0; right: 0; bottom: 0; height: 7px; background: var(--charcoal); }

  /* Letterhead */
  .letterhead {
    position: absolute; left: 674px; top: 100px; width: 428px; height: 604px;
    background: var(--paper);
  }
  .letterhead .brand-name { position: absolute; left: 39px; top: 42px; font-size: 23px; }
  .sender { position: absolute; left: 243px; top: 33px; }
  .sender-name { font-family: "Lora", serif; font-size: 15px; color: var(--charcoal); line-height: 18px; }
  .sender-line {
    display: flex; align-items: center; gap: 4px;
    font-family: "Roboto", sans-serif; font-size: 9.6px; color: var(--ink-dark); line-height: 13px;
  }
  .sender-line svg { width: 9px; height: 9px; flex: none; }

  .letter-body {
    position: absolute; left: 39px; top: 146px; width: 350px;
    font-size: 7.9px; line-height: 11.6px; color: var(--ink);
  }
  .letter-body p { margin-bottom: 11.6px; text-align: justify; text-align-last: left; }
  .letter-body .salutation { margin-bottom: 11.6px; }

  .letter-footer {
    position: absolute; left: 0; right: 0; top: 568px; display: flex; justify-content: center; align-items: center; gap: 4px;
    font-family: "Roboto", sans-serif; font-size: 9.2px; color: var(--ink-dark); white-space: nowrap;
  }
  .letter-footer svg { width: 9px; height: 9px; flex: none; }
  .letter-footer .gap { width: 3px; }
  .letterhead .edge-band { position: absolute; left: 0; right: 0; bottom: 0; height: 7px; background: var(--charcoal); }
</style>
</head>
<body>

  <div class="envelope-back">
    <svg width="451" height="229" viewBox="0 0 451 229" aria-hidden="true">
      <path d="M25 85 L3 229" stroke="var(--envelope-shade)" stroke-width="1" fill="none"/>
      <path d="M426 85 L440 150" stroke="var(--envelope-shade)" stroke-width="1" fill="none"/>
      <path d="M0 0 H451 L431 74 Q428 85 416 85 H35 Q23 85 20 74 Z" fill="var(--charcoal)"/>
    </svg>
    <div class="brand-name">Brandell Law</div>
  </div>

  <div class="envelope-front">
    <div class="brand-name">Brandell Law</div>
    <div class="return-address">PLLC 2750 Whitcombe, Suite 410 Dallas, Texas 75219</div>
    <div class="edge-band"></div>
  </div>

  <div class="letterhead">
    <div class="brand-name">Brandell Law</div>

    <div class="sender">
      <div class="sender-name">Douglas Brandell</div>
      <div class="sender-line">
        <svg viewBox="0 0 10 10" aria-hidden="true"><path d="M2.2 1 L3.8 2.6 L3 3.8 Q4 5.9 6.2 7 L7.4 6.2 L9 7.8 L8 9 Q4.5 9 1 2 Z" fill="none" stroke="var(--charcoal)" stroke-width="1.1"/></svg>
        <span>214 555 0186</span>
      </div>
      <div class="sender-line">
        <svg viewBox="0 0 10 10" aria-hidden="true"><rect x="0.6" y="1.8" width="8.8" height="6.4" fill="none" stroke="var(--charcoal)" stroke-width="1"/><path d="M0.6 1.8 L5 5.6 L9.4 1.8" fill="none" stroke="var(--charcoal)" stroke-width="1"/></svg>
        <span>douglas@brandell-legal.example</span>
      </div>
    </div>

    <div class="letter-body">
      <div class="salutation">Dear customer,</div>
      <p>Lorem ipsum dolor sit amet, consectetur adipisicing elit, sed do eiusmod tempor incididunt ut labore et dolore magna aliqua. Ut enim ad minim veniam, quis nostrud exercitation ullamco laboris nisi ut aliquip ex ea commodo consequat. Duis aute irure dolor in reprehenderit in voluptate velit esse cillum dolore eu fugiat nulla pariatur. Excepteur sint occaecat cupidatat non proident, sunt in culpa qui officia deserunt mollit anim id est laborum.</p>
      <p>Lorem ipsum dolor sit amet, consectetur adipisicing elit, sed do eiusmod tempor incididunt ut labore et dolore magna aliqua. Ut enim ad minim veniam, quis nostrud exercitation ullamco laboris nisi ut aliquip ex ea commodo consequat. Duis aute irure dolor in reprehenderit in voluptate velit esse cillum dolore eu fugiat nulla pariatur. Excepteur sint occaecat cupidatat non proident, sunt in culpa qui officia deserunt mollit anim id est laborum.</p>
      <p>Lorem ipsum dolor sit amet, consectetur adipisicing elit, sed do eiusmod tempor incididunt ut labore et dolore magna aliqua. Ut enim ad minim veniam, quis nostrud exercitation ullamco laboris nisi ut aliquip ex ea commodo consequat. Duis aute irure dolor in reprehenderit in voluptate velit esse cillum dolore eu fugiat nulla pariatur. Excepteur sint occaecat cupidatat non proident, sunt in culpa qui officia deserunt mollit anim id est laborum.</p>
      <p>Lorem ipsum dolor sit amet, consectetur adipisicing elit, sed do eiusmod tempor incididunt ut labore et dolore magna aliqua. Ut enim ad minim veniam, quis nostrud exercitation ullamco laboris nisi ut aliquip ex ea commodo consequat. Duis aute irure dolor in reprehenderit.</p>
      <div class="closing">Yours Sincerely,</div>
    </div>

    <div class="letter-footer">
      <svg viewBox="0 0 10 10" aria-hidden="true"><path d="M5 9.6 L1.9 5 A3.6 3.6 0 1 1 8.1 5 Z" fill="var(--charcoal)"/><circle cx="5" cy="3.6" r="1.3" fill="var(--paper)"/></svg>
      <span>PLLC 2750 Whitcombe, Suite 410 Dallas, Texas 75219</span>
      <span class="gap"></span>
      <svg viewBox="0 0 10 10" aria-hidden="true"><circle cx="5" cy="5" r="4.3" fill="none" stroke="var(--charcoal)" stroke-width="1.1"/><path d="M0.7 5 H9.3 M5 0.7 Q2.4 5 5 9.3 M5 0.7 Q7.6 5 5 9.3" fill="none" stroke="var(--charcoal)" stroke-width="0.8"/></svg>
      <span>www.brandell-legal.example</span>
    </div>

    <div class="edge-band"></div>
  </div>

</body>
</html>
```